Harlow K420 xl Cargo truck wrap for a masonry and concrete materials distributor

**THE VEHICLE IS A HARLOW VOYAGER K420 EXTENDED, TALL ROOF, WHITE IN COLOR.

We are looking for a full or half truck wrap showcasing who we are and what we sell. We would like to integrate your logo colours included in some black and white photos depicting what we sell and/or to which trade.
We distribute specialised construction materials and accessories for concrete and masonry restoration professionals. We specialty sell ciments, concretes, membranes, tools & accessories. we can supply some photos as examples but do not belong to us. We would like to have someone elses visual take on this project.

Target Market(s)

masons and concrete restoration specialists (heritage/ ancestral masonry repairs)

Industry/Entity Type

distribution construction materials

Requirements
Must have
• Logos in colour and pictures in black and white, must look like a distributor
Nice to have
• See ideas in project description. Stone wall, old brick and concrete repairs etc...
Should not have
• should not look like a contractors truck (we sell products not install them)

```html
<!DOCTYPE html>
<html lang="en">
<head>
<meta charset="utf-8">
<title>Stonehold – Harlow Voyager K420 wrap layout</title>
<link rel="stylesheet" href="https://fonts.googleapis.com/css2?family=Poppins:ital,wght@0,600;0,700;0,800;1,600;1,700&display=swap">
<style>
  :root {
    --orange: #c8552a;
    --concrete: #cfd0ce;
    --concrete-light: #dcdddb;
    --slate: #5b5c5e;
    --slate-dark: #3e3f41;
    --ink: #2c2c2c;
    --white: #f4f4f2;
    --brick-light: #d9c2a6;
    --brick-mid: #bfa585;
    --page: #ffffff;
  }
  * { box-sizing: border-box; margin: 0; padding: 0; }
  html, body { width: 1200px; height: 1200px; overflow: hidden; background: var(--page); }
  body { font-family: "Poppins", sans-serif; position: relative; }

  .wrap-panel {
    position: absolute;
    left: 80px;
    width: 1040px;
    height: 420px;
    border-radius: 18px;
    overflow: hidden;
    background: linear-gradient(180deg, var(--concrete-light), var(--concrete));
    box-shadow: 0 0 0 1px #b9bab8;
  }
  .wrap-panel--passenger { top: 130px; }
  .wrap-panel--driver { top: 650px; }

  .brick-photo {
    position: absolute;
    top: 0; bottom: 0;
    width: 330px;
    background: linear-gradient(160deg, var(--brick-light), var(--brick-mid));
  }
  .wrap-panel--passenger .brick-photo {
    left: 0;
    clip-path: polygon(0 0, 92% 0, 88% 18%, 95% 35%, 86% 55%, 100% 72%, 90% 88%, 97% 100%, 0 100%);
  }
  .wrap-panel--driver .brick-photo {
    right: 0;
    clip-path: polygon(8% 0, 100% 0, 100% 100%, 3% 100%, 10% 88%, 0 72%, 14% 55%, 5% 35%, 12% 18%);
  }

  .headline {
    position: absolute;
    top: 30px;
    line-height: 1.02;
    white-space: nowrap;
  }
  .wrap-panel--passenger .headline { left: 30px; text-align: left; }
  .wrap-panel--driver .headline { right: 30px; text-align: right; }
  .headline__trade {
    font-weight: 800;
    font-size: 40px;
    color: var(--orange);
    -webkit-text-stroke: 1.5px var(--ink);
    letter-spacing: -0.5px;
  }
  .headline__role {
    font-weight: 700;
    font-style: italic;
    font-size: 36px;
    color: var(--slate);
    -webkit-text-stroke: 1px var(--ink);
  }

  .connector {
    position: absolute;
    top: 55px;
    height: 3px;
    background: var(--orange);
  }
  .wrap-panel--passenger .connector { left: 320px; width: 182px; }
  .wrap-panel--driver .connector { left: 600px; width: 130px; }

  .web-pill {
    position: absolute;
    top: 36px;
    height: 40px;
    padding: 0 22px;
    border-radius: 20px;
    background: var(--orange);
    color: var(--white);
    font-weight: 700;
    font-style: italic;
    font-size: 24px;
    line-height: 40px;
    white-space: nowrap;
  }
  .wrap-panel--passenger .web-pill { left: 500px; }
  .wrap-panel--driver .web-pill { left: 280px; }

  .brand {
    position: absolute;
    top: 110px;
    display: flex;
    align-items: center;
    gap: 18px;
    white-space: nowrap;
  }
  .wrap-panel--passenger .brand { left: 340px; }
  .wrap-panel--driver .brand { left: 180px; }
  .brand__square { width: 70px; height: 70px; background: var(--orange); }
  .brand__name {
    font-weight: 800;
    font-size: 66px;
    color: var(--slate-dark);
    letter-spacing: 1px;
  }

  .product-band {
    position: absolute;
    top: 248px;
    height: 30px;
    background: var(--slate);
    color: var(--white);
    font-weight: 600;
    font-style: italic;
    font-size: 15px;
    line-height: 30px;
    display: flex;
    gap: 8px;
    padding: 0 20px;
    white-space: nowrap;
  }
  .wrap-panel--passenger .product-band { left: 20px; width: 740px; }
  .wrap-panel--driver .product-band { right: 20px; width: 820px; justify-content: flex-end; }
  .product-band__sep { color: var(--orange); }

  .phone {
    position: absolute;
    top: 310px;
    font-weight: 800;
    font-size: 38px;
    color: var(--orange);
    -webkit-text-stroke: 1.2px var(--ink);
    white-space: nowrap;
  }
  .wrap-panel--passenger .phone { left: 410px; }
  .wrap-panel--driver .phone { left: 330px; }
</style>
</head>
<body>

<section class="wrap-panel wrap-panel--passenger" aria-label="Harlow Voyager K420 passenger side wrap">
  <div class="brick-photo" role="img" aria-label="Black and white photo of an old brick wall in warm tan tones"></div>
  <div class="headline">
    <div class="headline__trade">MASONS AND<br>CONCRETE</div>
    <div class="headline__role">Restoration<br>Specialists</div>
  </div>
  <div class="connector"></div>
  <div class="web-pill">stonehold-supply.com</div>
  <div class="brand"><span class="brand__square"></span><span class="brand__name">STONEHOLD</span></div>
  <div class="product-band">
    <span>Ciments</span><span class="product-band__sep">-</span>
    <span>Concretes</span><span class="product-band__sep">-</span>
    <span>Membranes</span><span class="product-band__sep">-</span>
    <span>Tools &amp; Accessories</span>
  </div>
  <div class="phone">(555) 014-2271</div>
</section>

<section class="wrap-panel wrap-panel--driver" aria-label="Harlow Voyager K420 driver side wrap">
  <div class="brick-photo" role="img" aria-label="Black and white photo of an old brick wall in warm tan tones"></div>
  <div class="connector"></div>
  <div class="web-pill">stonehold-supply.com</div>
  <div class="headline">
    <div class="headline__trade">MASONS AND<br>CONCRETE</div>
    <div class="headline__role">Restoration<br>Specialists</div>
  </div>
  <div class="brand"><span class="brand__square"></span><span class="brand__name">STONEHOLD</span></div>
  <div class="product-band">
    <span>Ciments</span><span class="product-band__sep">-</span>
    <span>Concretes</span><span class="product-band__sep">-</span>
    <span>Membranes</span><span class="product-band__sep">-</span>
    <span>Tools &amp; Accessories</span>
  </div>
  <div class="phone">(555) 014-2271</div>
</section>

</body>
</html>
```